REX DUNMORE INSTITUTE

I need one trifold brochure that can describe our company and what we do. Our site is www.rexdunmoreinstitute.example Right now there is just one program we offer. A 52 week leadership development program called "Crafting Your Remarkable Path". The way our program works is you enroll for 97.95 and then you receive an email each week with a pdf file of a lesson and a video from one of our experts discussing the lesson. Its like Gary Pellman meets zel forums meets linkbook. We have a leader in Rex Dunmore, video segmets from our experts in a community of thousands.
Leadership

```html
<!DOCTYPE html>
<html lang="en">
<head>
<meta charset="utf-8">
<title>Rex Dunmore Institute – Trifold Brochure</title>
<link rel="stylesheet" href="https://fonts.googleapis.com/css2?family=Arimo:wght@400;700&family=Didact+Gothic&display=swap">
<style>
  :root {
    --ink: #111111;
    --panel-black: #000000;
    --bar-dark: #2e2e2e;
    --accent-blue: #27a9e1;
    --paper: #ffffff;
    --stage: #eeeeee;
    --text-light: #ffffff;
    --partner-red: #e3222b;
    --logo-blue: #2f6fb5;
    --photo-dark: #1d1a19;
    --photo-skin: #c98c74;
  }
  * { box-sizing: border-box; margin: 0; padding: 0; }
  html, body { width: 1200px; height: 1000px; overflow: hidden; }
  body {
    background: var(--stage);
    font-family: "Didact Gothic", "Century Gothic", sans-serif;
    color: var(--ink);
    position: relative;
  }
  .spread {
    position: absolute;
    top: 285px;
    width: 560px;
    height: 430px;
    background: var(--paper);
    box-shadow: 0 2px 8px rgba(0,0,0,.12);
  }
  .spread--outside { left: 20px; }
  .spread--inside { left: 620px; }

  .bar { position: absolute; left: 0; width: 100%; height: 19px; background: var(--bar-dark); }
  .bar--top { top: 0; border-bottom: 3px solid var(--accent-blue); height: 22px; }
  .bar--bottom { bottom: 0; }

  .black-band {
    position: absolute; left: 0; top: 114px; width: 100%; height: 222px;
    background: var(--panel-black);
  }
  .col { position: absolute; width: 186px; }
  .col--1 { left: 0; }
  .col--2 { left: 187px; }
  .col--3 { left: 374px; }

  .heading {
    font-family: "Arimo", Arial, sans-serif;
    font-weight: 700;
    font-size: 10px;
    line-height: 1.2;
    color: var(--ink);
  }
  .body-copy {
    font-size: 6.4px;
    line-height: 1.32;
    color: var(--text-light);
  }
  .body-copy p + p { margin-top: 6px; }

  /* Outside spread */
  .movement-title { position: absolute; left: 18px; top: 48px; }
  .movement-ask { position: absolute; left: 18px; top: 72px; width: 150px; font-size: 8px; line-height: 1.3; }
  .experts-title { position: absolute; left: 175px; top: 74px; }
  .brand-lockup {
    position: absolute; left: 378px; top: 30px;
    display: flex; align-items: center; gap: 6px;
    font-size: 13px; color: var(--ink);
  }
  .brand-mark { width: 14px; height: 14px; background: var(--logo-blue); }
  .cover-quote {
    position: absolute; left: 386px; top: 62px; width: 170px;
    font-family: "Arimo", Arial, sans-serif; font-weight: 700; font-size: 8.6px; line-height: 1.25;
  }
  .cover-quote .sig { display: block; margin-top: 5px; }

  .movement-copy { left: 16px; top: 126px; width: 160px; }
  .experts-copy { left: 187px; top: 120px; width: 165px; }
  .photo { position: absolute; }
  .photo--cover {
    left: 490px; top: 122px; width: 64px; height: 72px;
    background: linear-gradient(180deg, #0d0d0d 0%, #2a2524 60%, #3b3737 100%);
  }
  .cover-name {
    position: absolute; left: 400px; top: 160px;
    display: flex; align-items: center; gap: 5px;
    font-size: 11px; color: var(--text-light);
  }
  .cover-name .brand-mark { width: 11px; height: 11px; }
  .cover-points {
    position: absolute; left: 394px; top: 212px; width: 160px;
    list-style: none; font-size: 6.8px; line-height: 1.3; color: var(--text-light);
  }
  .cover-points li { position: relative; padding-left: 9px; margin-bottom: 7px; }
  .cover-points li::before { content: ""; position: absolute; left: 1px; top: 2.5px; width: 3px; height: 3px; border-radius: 50%; background: var(--text-light); }
  .cover-cta {
    position: absolute; left: 430px; top: 306px;
    font-family: "Arimo", Arial, sans-serif; font-weight: 700; font-size: 10px; color: var(--text-light);
  }
  .footer-line { position: absolute; left: 18px; top: 354px; width: 165px; font-size: 7px; line-height: 1.3; }
  .footer-others { position: absolute; left: 280px; top: 348px; font-size: 7.4px; }
  .partner-label { position: absolute; left: 405px; top: 354px; font-size: 5.6px; letter-spacing: .3px; }
  .partner-badge { position: absolute; left: 406px; top: 364px; width: 78px; height: 28px; background: var(--partner-red); }

  /* Inside spread */
  .story-title { position: absolute; left: 18px; top: 52px; font-size: 10.5px; }
  .photo--story {
    left: 102px; top: 38px; width: 66px; height: 58px;
    background: linear-gradient(180deg, var(--photo-dark) 0%, #3a2624 55%, #b8352e 100%);
  }
  .mission-title { position: absolute; left: 218px; top: 60px; }
  .lessons-title { position: absolute; left: 405px; top: 60px; }
  .story-copy { left: 16px; top: 122px; width: 160px; }
  .mission-copy { left: 192px; top: 122px; width: 160px; }
  .lessons-copy { left: 376px; top: 106px; width: 172px; }
  .band-extension { position: absolute; left: 372px; top: 100px; width: 188px; height: 20px; background: var(--panel-black); }
  .lessons-copy ul { list-style: none; margin-top: 2px; padding-left: 8px; }
  .lessons-copy li { position: relative; padding-left: 8px; }
  .lessons-copy li::before { content: ""; position: absolute; left: 0; top: 2.5px; width: 3px; height: 3px; border-radius: 50%; background: var(--text-light); }

  .inside-join { position: absolute; left: 90px; top: 355px; font-size: 7.4px; }
  .receive { position: absolute; left: 192px; top: 338px; width: 170px; font-size: 5.8px; line-height: 1.35; }
  .receive ul { list-style: none; }
  .receive li::before { content: "• "; }
  .receive .price { font-family: "Arimo", Arial, sans-serif; font-weight: 700; margin-top: 4px; display: block; }
  .no-excuses { position: absolute; left: 384px; top: 350px; font-size: 6.4px; }
  .start-today { position: absolute; left: 448px; top: 367px; font-size: 8px; }
</style>
</head>
<body>

<section class="spread spread--outside" aria-label="Brochure outside spread">
  <div class="bar bar--top"></div>
  <div class="black-band"></div>

  <h2 class="heading movement-title">The movement</h2>
  <p class="movement-ask">“What is it exactly?” some of you may be asking yourselves.</p>
  <h2 class="heading experts-title">Meet A Few Of Our Experts</h2>

  <div class="brand-lockup"><span class="brand-mark"></span>Rex Dunmore Institute</div>
  <p class="cover-quote">“One Goal, Well Executed, Could Change Your Life Forever.”<span class="sig">Dr. Rex Dunmore</span></p>

  <div class="col body-copy movement-copy">
    <p>Let's begin by taking a minute or two out of your busy day to consider the following questions as I lay out our vision of “The Movement” for you. Suppose one day you decide that the life you are leading, a life that has had its share of relative successes, is not all that you had envisioned? Suppose one day, YOU decide there is more to life than this, that there is more for your family because they deserve it, there is more for your community because it needs it, there is more for you because you have dreamed of it?</p>
    <p>Each week you will be challenged and inspired to set specific goals toward achieving the life you have always imagined. Each week Dr. Dunmore will break down the steps you will take, plus you will have access to his vast array of fellow business advisors, life coaches and successful, self-made business owners.</p>
  </div>

  <div class="col body-copy experts-copy">
    <p>Miles Carrow - works with hundreds of organizations to transform today's challenges into a foundation for incredible growth. Visit Miles Carrow at www.risingpath.example</p>
    <p>Hannah Brook Varela - With over 22 years of experience with Privately Owned Growth Enterprises, Hannah has worked with owners to develop sustained business value growth in both the United States and Canada through entrepreneurial development, focused operational efficiency, effective management team development, enhanced financial management, measurement and accountability. Visit Hannah at www.varelaconsulting.example</p>
    <p>Dr. Owen Tarr - is considered to be one of the premier performance coaches in the United States. Visit Dr. Owen at www.tarrperformance.example</p>
  </div>

  <div class="photo photo--cover" role="img" aria-label="Portrait photograph of Dr. Rex Dunmore"></div>
  <div class="cover-name"><span class="brand-mark"></span>Rex Dunmore</div>
  <ul class="cover-points">
    <li>What Are Your Goals For Next Year?</li>
    <li>How Do You Plan To Achieve Them?</li>
    <li>Our Process Will Help You Create And Execute Your Life Goals</li>
  </ul>
  <p class="cover-cta">Join The Movement....</p>

  <p class="footer-line">Join the Movement and change your life from common to EXCEPTIONAL.</p>
  <p class="heading footer-others">And Many Others</p>
  <p class="partner-label">IN PARTNERSHIP WITH</p>
  <div class="partner-badge" role="img" aria-label="Partner badge"></div>

  <div class="bar bar--bottom"></div>
</section>

<section class="spread spread--inside" aria-label="Brochure inside spread">
  <div class="bar bar--top"></div>
  <div class="black-band"></div>
  <div class="band-extension"></div>

  <h2 class="heading story-title">Dr. Rex Dunmore:<br>Rex's Story</h2>
  <div class="photo photo--story" role="img" aria-label="Portrait photograph of Dr. Rex Dunmore in a red shirt"></div>
  <h2 class="heading mission-title">Rex's Mission</h2>
  <h2 class="heading lessons-title">Rex's Lessons</h2>

  <div class="col body-copy story-copy">
    <p>After 26 years in public education and at 50 years of age, Dr. Rex Dunmore left Lakeview State University, where he was a professor and administrator, to pursue an entrepreneurial career in real estate franchise sales. In less than 10 years, the real estate offices combined did more than $3 billion in sales. He sold his company in 1999 and now spends his time and energy giving back what he learned in becoming what he is today.</p>
    <p>Rex is a husband, father, grandfather, airplane pilot, marathon runner, mountain climber, skydiver, writer and speaker.</p>
    <p>He is the author of Life at the Ridge, co-author of the companion workbook Life Plan and is co-author of Warm Broth for the Founder's Spirit. It is currently available in bookstores and though Shopmart.example.</p>
  </div>

  <div class="col body-copy mission-copy">
    <p>My friends, why is it that some people figure it out and others don't? How come it seems that some people are “on a path” and others seem to flounder? I believe my education, my business experience and my coaching clients have proven to me that it comes down to understanding the principles of life and how they apply to your life.</p>
    <p>I want each and every one of you to reach your potential, maximize your peak performance, and find that inner drive that allows you to discover your talents and purpose!</p>
    <p>ENROLL today to start the planning process, review the Leadership Lessons and start planning for 2013. Then on January 4, 2013, you and 10,000 other people across the globe will share one common goal: to reach your goals and start designing the life you have always wanted.</p>
  </div>

  <div class="col body-copy lessons-copy">
    <p>My 52 Lessons are for those individuals who are ready to begin the process of working with my network of experts, advisors and mentors, essentially learning how to set goals and network with successful individuals who are on the same path. By design, you will receive a printable lesson, a video explanation of the lesson and the advice of our experts each week. You will receive suggested exercises for writing out your goals, recommended reading and key websites - and these are just a few of the tools you will receive each week.<br>You will set your goals by becoming aware of, gaining clarity of and developing mastery of the Six Life Priorities:</p>
    <ul>
      <li>Spirituality</li>
      <li>Health</li>
      <li>Relationships</li>
      <li>Emotions</li>
      <li>Professional</li>
      <li>Finances</li>
    </ul>
  </div>

  <p class="heading inside-join">Join The Movement</p>
  <div class="receive">
    <p>You will receive:</p>
    <ul>
      <li>My 1st Edition Leadership Lessons (52 in total)</li>
      <li>My Weekly Newsletter</li>
      <li>Enrollment into our 2013 Goal Planning Movement</li>
    </ul>
    <span class="price">All of this for $97.95 - less than 2 dollars per week!</span>
  </div>
  <p class="no-excuses">No excuses - you deserve an Exceptional Life!</p>
  <p class="heading start-today">Start planning today!</p>

  <div class="bar bar--bottom"></div>
</section>

</body>
</html>
```